Banner Ad for Weight Loss Product Site

We need a banner ad design for a new company selling a weight loss online programme (Ebook). The product is called "Your FitRoute" and is suitable for people that want to lose weight fast and without doing sports, regardless of age. We would like to see designs that are eye-catching and at its best animated like in the example files. The final design should exhibit a professional look that encourages the customers to buy our product. The text should be "Persönlicher Diätplan zum Abnehmen?" as a title and "Jetzt informieren" for the button field. Thank you!

```html
<!DOCTYPE html>
<html lang="de">
<head>
<meta charset="utf-8">
<title>Your FitRoute – Banner</title>
<link rel="stylesheet" href="https://fonts.googleapis.com/css2?family=Source+Sans+3:wght@400;600;700&display=swap">
<style>
  :root {
    --canvas: #ffffff;
    --ink: #111111;
    --brand-green: #4a6a12;
    --brand-orange: #f58a1f;
    --ring-orange: #f6a300;
    --white: #ffffff;
    --photo-top: #d8b7a0;
    --photo-bottom: #a88470;
  }
  html, body {
    margin: 0;
    padding: 0;
    overflow: hidden;
    background: var(--canvas);
  }
  .canvas {
    display: block;
    width: 673px;
    height: 1200px;
  }
  .board-frame { fill: none; stroke: var(--ink); stroke-width: 1.5; }
  .divider { stroke: var(--ink); stroke-width: 1.2; }
  .variant-label {
    font-family: "Source Sans 3", Arial, sans-serif;
    font-size: 11px;
    fill: var(--ink);
    text-anchor: middle;
  }
  .badge-dark { fill: var(--brand-green); stroke: var(--ring-orange); stroke-width: 6; }
  .badge-light { fill: var(--white); stroke: var(--brand-green); stroke-width: 6; }
  .brand-ring { fill: none; stroke: var(--white); stroke-width: 1.4; }
  .brand-disc { fill: var(--brand-green); }
  .brand-name {
    font-family: "Source Sans 3", Arial, sans-serif;
    font-weight: 600;
    fill: var(--white);
    text-anchor: middle;
  }
  .brand-name-large { font-size: 22px; }
  .brand-name-small { font-size: 18px; }
  .headline {
    font-family: "Source Sans 3", Arial, sans-serif;
    font-weight: 600;
    font-size: 26px;
    text-anchor: middle;
  }
  .headline-on-dark { fill: var(--white); }
  .headline-on-light { fill: var(--brand-orange); }
  .cta-button { fill: var(--brand-orange); }
  .cta-label {
    font-family: "Source Sans 3", Arial, sans-serif;
    font-weight: 700;
    font-size: 21px;
    fill: var(--white);
  }
  .photo-outline { fill: var(--white); }
  .photo-fill { fill: url(#photoTone); }
</style>
</head>
<body>
<svg class="canvas" viewBox="0 0 673 1200" xmlns="http://www.w3.org/2000/svg">
  <defs>
    <linearGradient id="photoTone" x1="0" y1="0" x2="0" y2="1">
      <stop offset="0" stop-color="var(--photo-top)"/>
      <stop offset="1" stop-color="var(--photo-bottom)"/>
    </linearGradient>
  </defs>

  <rect class="board-frame" x="17" y="17" width="640" height="1160"/>

  <!-- Variant A: green badge -->
  <g class="variant variant-dark">
    <text class="variant-label" x="337" y="95">OP-1</text>
    <circle class="badge-dark" cx="345" cy="335" r="205"/>
    <g class="brand-mark">
      <circle class="brand-ring" cx="273" cy="241" r="64"/>
      <text class="brand-name brand-name-large">
        <tspan x="273" y="236">Your</tspan>
        <tspan x="273" y="261">FitRoute</tspan>
      </text>
    </g>
    <text class="headline headline-on-dark">
      <tspan x="264" y="351">Persönlicher</tspan>
      <tspan x="264" y="380">Diätplan zum</tspan>
      <tspan x="264" y="409">Abnehmen?</tspan>
    </text>
    <rect class="cta-button" x="127" y="436" width="366" height="33" rx="4"/>
    <text class="cta-label" x="140" y="460">JETZT INFORMIEREN</text>
    <g class="model-photo" role="img" aria-label="Foto einer lächelnden Frau in Sportkleidung mit Maßband um die Taille, die auf den Betrachter zeigt">
      <rect class="photo-outline" x="362" y="146" width="152" height="377" rx="40"/>
      <rect class="photo-fill" x="367" y="151" width="142" height="367" rx="36"/>
    </g>
  </g>

  <line class="divider" x1="77" y1="590" x2="605" y2="590"/>

  <!-- Variant B: white badge -->
  <g class="variant variant-light">
    <text class="variant-label" x="337" y="648">OP-1</text>
    <circle class="badge-light" cx="345" cy="882" r="206"/>
    <g class="brand-mark">
      <circle class="brand-disc" cx="276" cy="779" r="51"/>
      <text class="brand-name brand-name-small">
        <tspan x="276" y="775">Your</tspan>
        <tspan x="276" y="796">FitRoute</tspan>
      </text>
    </g>
    <text class="headline headline-on-light">
      <tspan x="267" y="894">Persönlicher</tspan>
      <tspan x="267" y="923">Diätplan zum</tspan>
      <tspan x="267" y="952">Abnehmen?</tspan>
    </text>
    <rect class="cta-button" x="127" y="979" width="366" height="34" rx="4"/>
    <text class="cta-label" x="140" y="1004">JETZT INFORMIEREN</text>
    <g class="model-photo" role="img" aria-label="Foto einer lächelnden Frau in Sportkleidung mit Maßband um die Taille, die auf den Betrachter zeigt">
      <rect class="photo-fill" x="366" y="696" width="142" height="371" rx="36"/>
    </g>
  </g>
</svg>
</body>
</html>
```